Business card for Full Stable Care Vandorpe

I would like to have me designed an professional business card with my existing logo for my company called : full stable care vandorpe gcv.
I prefer a two sided business card with on the back side only the horses head and the website : fscvandorpe-example.eu
Only one colour shouldbe all right.
The logo must appear in a nic professional way on the business card.

Other suggestion are welcome.

All copy wrights must be released by the designer after we have selected a final design.

Target Market(s)

Equestrian businesses

Industry/Entity Type

Business

Contact Information for Business Card

Laurent Vandorpe
Title: zaakvoerder
Full Stable Care Vandorpe GCV
Molkenweg 47
B - 3190 Herselmont
België
Phone: + 32 491 68 27 04
Mail: laurent@fscvandorpe-example.eu

Font styles to use
Serif

Requirements
Must have
• My own logo
• See attached files
• Website: fscvandorpe-example.eu

```html
<!DOCTYPE html>
<html lang="nl">
<head>
<meta charset="utf-8">
<title>Full Stable Care Vandorpe – Business Card</title>
<link rel="stylesheet" href="https://fonts.googleapis.com/css2?family=Cinzel:wght@700&family=Open+Sans:wght@400;700&display=swap">
<style>
  :root {
    --backdrop: #3b3b3d;
    --card: #231f20;
    --ink: #ffffff;
    --ink-soft: #e8e8e8;
  }
  * { box-sizing: border-box; margin: 0; padding: 0; }
  html, body { width: 1200px; height: 900px; overflow: hidden; background: var(--backdrop); }
  .canvas {
    position: relative; width: 1200px; height: 900px;
    display: flex; justify-content: center; align-items: center; gap: 70px;
  }
  .card {
    position: relative; width: 340px; height: 520px;
    background: var(--card); border-radius: 26px; color: var(--ink);
  }
  .card--front { display: flex; align-items: center; justify-content: center; padding-top: 30px; }
  .brand-name {
    font-family: "Cinzel", Georgia, serif; font-weight: 700;
    font-size: 25px; line-height: 1.2; text-align: center; letter-spacing: 0.5px;
    color: var(--ink);
  }
  .card--back { padding: 12px; }
  .card__frame {
    position: absolute; inset: 12px; border: 1.5px solid var(--ink);
    border-radius: 20px;
  }
  .card__content {
    position: relative; height: 100%;
    display: flex; flex-direction: column; align-items: center;
    padding-top: 70px; font-family: "Open Sans", Arial, sans-serif;
  }
  .brand-mark { display: flex; align-items: center; gap: 10px; margin-bottom: 26px; }
  .brand-mark__dot { width: 22px; height: 22px; border-radius: 50%; background: var(--ink); }
  .brand-mark__name {
    font-family: "Cinzel", Georgia, serif; font-weight: 700; font-size: 15px;
    line-height: 1.25; color: var(--ink);
  }
  .name-ribbon { position: relative; width: 230px; height: 30px; margin-bottom: 4px; }
  .name-ribbon svg { position: absolute; inset: 0; }
  .name-ribbon__text {
    position: relative; display: block; text-align: center; line-height: 30px;
    color: var(--card); font-weight: 700; font-size: 16px;
  }
  .job-title { font-size: 12px; color: var(--ink-soft); margin-bottom: 20px; }
  .contact { text-align: center; font-size: 12.5px; line-height: 1.45; color: var(--ink-soft); }
  .contact__address { margin-bottom: 12px; }
  .contact__rule { width: 80px; height: 2px; background: var(--ink); margin: 6px auto 0; }
</style>
</head>
<body>
<main class="canvas">
  <section class="card card--front" aria-label="Card front">
    <p class="brand-name">Full Stable Care<br>Vandorpe</p>
  </section>

  <section class="card card--back" aria-label="Card back">
    <div class="card__frame"></div>
    <div class="card__content">
      <div class="brand-mark">
        <span class="brand-mark__dot"></span>
        <span class="brand-mark__name">Full Stable Care<br>Vandorpe</span>
      </div>
      <div class="name-ribbon">
        <svg width="230" height="30" viewBox="0 0 230 30" aria-hidden="true">
          <polygon points="6,15 14,7 22,15 14,23" fill="#ffffff"/>
          <polygon points="24,4 206,4 206,26 24,26 30,15" fill="#ffffff"/>
          <polygon points="208,15 216,7 224,15 216,23" fill="#ffffff"/>
        </svg>
        <span class="name-ribbon__text">Laurent Vandorpe</span>
      </div>
      <p class="job-title">zaakvoerder</p>
      <div class="contact">
        <p class="contact__address">Molkenweg 47,<br>B - 3190 Herselmont, België</p>
        <p>+ 32 491 68 27 04</p>
        <p>laurent@fscvandorpe-example.eu</p>
        <p>www.fscvandorpe-example.eu</p>
        <div class="contact__rule"></div>
      </div>
    </div>
  </section>
</main>
</body>
</html>
```